Veterinary Business cards

Redesign Business Card

Information needed on Card:
Hours: Mon-Fri: 4pm -10PM; Sat- Sun- 10 AM- 5PM
Help@bayfernvet.com
www.bayfernvet.com
555-718-2946
4173 SE 19th Ave. okc, ok 73958
*No appointment necessary*

Optional:
Our tag line is "We're here when you need us" - If it fits on the cards.

```html
<!DOCTYPE html>
<html lang="en">
<head>
<meta charset="utf-8">
<title>Bayfern Urgent Care – Business Cards</title>
<link href="https://fonts.googleapis.com/css2?family=Montserrat:wght@400;500;700&family=Oswald:wght@500&family=Libre+Baskerville&display=swap" rel="stylesheet">
<style>
  :root {
    --navy: #1b3d6b;
    --orange: #d77a1a;
    --white: #ffffff;
    --backdrop: #3a3a3c;
  }
  html, body {
    margin: 0;
    width: 1200px;
    height: 998px;
    overflow: hidden;
    background: var(--backdrop);
    font-family: "Montserrat", sans-serif;
  }
  .card {
    position: absolute;
    left: 250px;
    width: 700px;
    height: 400px;
    overflow: hidden;
    box-shadow: 0 10px 30px rgba(0,0,0,0.45);
  }
  .card--front { top: 60px; background: var(--navy); }
  .card--back { top: 530px; background: var(--white); }

  .brand {
    position: absolute;
    display: flex;
    align-items: center;
    gap: 12px;
    font-family: "Montserrat", sans-serif;
    font-weight: 500;
    letter-spacing: 0.05em;
    white-space: nowrap;
  }
  .brand__dot { border-radius: 50%; background: var(--orange); flex: none; }
  .card--front .brand {
    left: 0; right: 0; top: 140px;
    justify-content: center;
    color: var(--white);
    font-size: 40px;
  }
  .card--front .brand__dot { width: 30px; height: 30px; }
  .tagline {
    position: absolute;
    left: 0; right: 0; top: 300px;
    margin: 0;
    text-align: center;
    color: var(--white);
    font-family: "Libre Baskerville", serif;
    font-size: 22px;
  }

  .back-art { position: absolute; inset: 0; }
  .card--back .brand {
    left: 40px; top: 152px;
    color: var(--navy);
    font-size: 22px;
  }
  .card--back .brand__dot { width: 18px; height: 18px; }

  .contact {
    position: absolute;
    right: 24px; top: 42px;
    text-align: right;
    color: var(--white);
    font-size: 13.5px;
    line-height: 1.55;
  }
  .contact__name {
    font-family: "Oswald", sans-serif;
    font-weight: 500;
    color: var(--orange);
    font-size: 26px;
    line-height: 1.15;
    text-transform: uppercase;
  }
  .contact__row { display: flex; justify-content: flex-end; align-items: center; gap: 7px; }
  .contact__icon { width: 13px; height: 13px; flex: none; }
  .contact__note { font-weight: 700; margin-top: 2px; }
  .hours {
    position: absolute;
    right: 22px; bottom: 13px;
    color: var(--orange);
    font-weight: 700;
    font-size: 15.5px;
    white-space: nowrap;
  }
</style>
</head>
<body>

<section class="card card--front">
  <div class="brand"><span class="brand__dot"></span>BAYFERN URGENT CARE</div>
  <p class="tagline">We're here when you need us</p>
</section>

<section class="card card--back">
  <svg class="back-art" viewBox="0 0 700 400" width="700" height="400" aria-hidden="true">
    <path transform="translate(-10 0)" d="M700 0 L600 0 C470 20 430 100 410 200 C390 300 350 340 260 352 C210 360 180 375 150 400 L700 400 Z" fill="var(--orange)"/>
    <path d="M700 0 L600 0 C470 20 430 100 410 200 C390 300 350 340 260 352 C210 360 180 375 150 400 L700 400 Z" fill="var(--navy)" stroke="var(--white)" stroke-width="2"/>
  </svg>

  <div class="brand"><span class="brand__dot"></span>BAYFERN URGENT CARE</div>

  <div class="contact">
    <div class="contact__name">Marcus Hale</div>
    <div>Managing Director</div>
    <div class="contact__row">555-718-2946
      <svg class="contact__icon" viewBox="0 0 16 16"><path d="M3 1h3l1.5 4-2 1.3a9 9 0 0 0 4.2 4.2L11 8.5l4 1.5v3a2 2 0 0 1-2 2A13 13 0 0 1 1 3a2 2 0 0 1 2-2z" fill="var(--orange)"/></svg>
    </div>
    <div class="contact__row">Help@bayfernvet.com
      <svg class="contact__icon" viewBox="0 0 16 16"><rect x="1" y="3" width="14" height="10" fill="var(--orange)"/><path d="M1 3l7 6 7-6" fill="none" stroke="var(--navy)" stroke-width="1.4"/></svg>
    </div>
    <div class="contact__row">www.bayfernvet.com
      <svg class="contact__icon" viewBox="0 0 16 16"><circle cx="8" cy="8" r="7" fill="var(--orange)"/><path d="M1 8h14M8 1c3 3 3 11 0 14M8 1c-3 3-3 11 0 14" fill="none" stroke="var(--navy)" stroke-width="1"/></svg>
    </div>
    <div>4173 SE 19th Ave. okc, ok 73958</div>
    <div class="contact__note">*No appointment necessary*</div>
  </div>

  <div class="hours">Hours: Mon-Fri: 4pm -10PM; Sat- Sun- 10 AM- 5PM</div>
</section>

</body>
</html>
```